Business Card for my building company

I would like the card to make a statement, so as soon as you see the card you think "wow nice card' and then read the details on the card its self. Also i would like to be able to put in the detail for the MUST HAVES so please Crete a box that i can alter depending on who in my business needs the cards. Thank you

Target Market(s)

Any one looking to build a house/ townhouse or duplex

Industry/Entity Type

Home Builder

Contact Information for Business Card

I would like the card to have the logo on the card and the must haves

Font styles to use
Sans Serif

Requirements
Must have
• Name
• Phone Number
• Email Address
• Website
• Licence Number
• Abn

```html
<!DOCTYPE html>
<html lang="en">
<head>
<meta charset="utf-8">
<title>Ridgeline Homes – Business Card</title>
<link rel="stylesheet" href="https://fonts.googleapis.com/css2?family=Arimo:wght@400;700&display=swap">
<style>
  :root {
    --bg: #e9e6e1;
    --card-black: #060606;
    --gold: #c9a44c;
    --white: #ffffff;
    --wall-light: #a59a8c;
    --wall-mid: #85796b;
    --wall-dark: #4e4339;
  }
  * { margin: 0; padding: 0; box-sizing: border-box; }
  html, body {
    width: 1200px; height: 960px; overflow: hidden;
    background: var(--bg);
    font-family: "Arimo", Arial, sans-serif;
  }
  .stage {
    width: 1200px; height: 960px;
    display: flex; align-items: center; justify-content: center;
  }
  .business-card {
    width: 1000px; height: 620px;
    display: flex;
    background: var(--card-black);
    box-shadow: 0 18px 40px rgba(0,0,0,0.25);
  }
  .brand-panel {
    position: relative;
    width: 400px; height: 100%;
    background: linear-gradient(180deg, var(--wall-light) 0%, var(--wall-mid) 70%, var(--wall-dark) 100%);
  }
  .brand-mark {
    position: absolute;
    left: 0; right: 0; bottom: 150px;
    display: flex; align-items: center; justify-content: center; gap: 14px;
  }
  .brand-mark .brand-square {
    width: 34px; height: 34px; background: var(--card-black);
  }
  .brand-mark .brand-name {
    font-weight: 700; font-size: 38px; color: var(--card-black);
    letter-spacing: 0.5px;
  }
  .gold-rule {
    width: 8px; height: 100%;
    background: var(--gold);
    margin-left: 14px;
  }
  .details-panel {
    flex: 1;
    padding: 70px 70px 60px 40px;
    display: flex; flex-direction: column; align-items: flex-end;
    text-align: right;
  }
  .person-name {
    font-size: 60px; font-weight: 700; color: var(--white); line-height: 1;
  }
  .person-title {
    font-size: 38px; color: var(--gold); margin-top: 6px;
  }
  .credentials {
    margin-top: 70px;
    font-size: 30px; color: var(--white); line-height: 1.3;
  }
  .contact-list {
    margin-top: 30px; list-style: none;
    font-size: 30px; color: var(--white); line-height: 1.35;
  }
  .contact-list li { display: flex; align-items: center; justify-content: flex-end; gap: 16px; }
  .contact-icon { width: 24px; height: 24px; flex: none; }
  .contact-list .no-icon { padding-right: 40px; }
</style>
</head>
<body>
<main class="stage">
  <article class="business-card">
    <section class="brand-panel" role="img" aria-label="Photo of a textured wall behind the company name">
      <div class="brand-mark">
        <span class="brand-square"></span>
        <span class="brand-name">Ridgeline Homes</span>
      </div>
    </section>
    <div class="gold-rule"></div>
    <section class="details-panel">
      <h1 class="person-name">Daniel Harlow</h1>
      <p class="person-title">Managing Director</p>
      <p class="credentials">Lic : 30418265<br>ABN : 582196</p>
      <ul class="contact-list">
        <li>021-555-0192
          <svg class="contact-icon" viewBox="0 0 24 24"><rect width="24" height="24" fill="var(--gold)"/><path d="M7 5h3l1 4-2 1.5a9 9 0 0 0 4.5 4.5L15 13l4 1v3a2 2 0 0 1-2 2A13 13 0 0 1 5 7a2 2 0 0 1 2-2z" fill="#060606"/></svg>
        </li>
        <li>ridgelinehomes.com
          <svg class="contact-icon" viewBox="0 0 24 24"><rect width="24" height="24" fill="var(--gold)"/><circle cx="12" cy="12" r="7" fill="none" stroke="#060606" stroke-width="1.8"/><path d="M5 12h14M12 5c-3 3.5-3 10.5 0 14M12 5c3 3.5 3 10.5 0 14" fill="none" stroke="#060606" stroke-width="1.5"/></svg>
        </li>
        <li>daniel@ridgelinehomes.com.au
          <svg class="contact-icon" viewBox="0 0 24 24"><rect width="24" height="24" fill="var(--gold)"/><rect x="5" y="7" width="14" height="10" fill="none" stroke="#060606" stroke-width="1.8"/><path d="M5 7l7 6 7-6" fill="none" stroke="#060606" stroke-width="1.8"/></svg>
        </li>
        <li class="no-icon">ridgelinehomes.com.au</li>
      </ul>
    </section>
  </article>
</main>
</body>
</html>
```